Deactivated Coal-Fired Power Plant to be redeveloped into a Green Energy Campus.

Want a striking business card statement that introduces our concept project to provide economic and community recovery to a former rural coal community in western PA.
Essentially 12 project representatives that will lead both the demolition of an existing power plant and the redevelopment to a new Green energy site.
Business Card should reflect our effort.
We are open to ideas.

Target Market(s)

Energy and Power Generation industries

Industry/Entity Type

Power Generation and Data Centers

Contact Information for Business Card

Font styles to use
Sans Serif
Other font styles liked:
• Arial, Calibri

Requirements
Must have
• Multiple colors

```html
<!DOCTYPE html>
<html lang="en">
<head>
<meta charset="utf-8">
<title>Ridgeview Renewal – Business Card</title>
<link href="https://fonts.googleapis.com/css2?family=Montserrat:wght@600&family=Arimo:wght@400;700&display=swap" rel="stylesheet">
<style>
  :root {
    --stage: #3a3a3a;
    --card: #2d2d2d;
    --green: #12934a;
    --white: #ffffff;
    --soft: #e6e6e6;
    --divider: #6a6a6a;
  }
  * { box-sizing: border-box; margin: 0; padding: 0; }
  html, body { width: 1200px; height: 689px; overflow: hidden; }
  body {
    background: var(--stage);
    position: relative;
    font-family: "Arimo", Arial, sans-serif;
  }
  .card {
    position: absolute;
    top: 190px;
    width: 540px;
    height: 309px;
    background: var(--card);
    border-radius: 16px;
    overflow: hidden;
  }
  .card--front { left: 40px; }
  .card--back { left: 620px; }

  .brand {
    display: flex;
    align-items: center;
    justify-content: center;
    gap: 14px;
  }
  .brand__dot {
    width: 34px; height: 34px;
    border-radius: 50%;
    background: var(--green);
    flex: none;
  }
  .brand__name {
    font-family: "Montserrat", sans-serif;
    font-weight: 600;
    color: var(--white);
    font-size: 30px;
    letter-spacing: 1px;
    line-height: 1;
  }

  .card--front .brand { margin-top: 118px; }
  .tagline {
    margin-top: 22px;
    text-align: center;
    font-family: "Montserrat", sans-serif;
    font-weight: 600;
    font-size: 13px;
    letter-spacing: 2px;
    color: var(--white);
  }
  .tagline__accent { color: var(--green); }

  .card--back .brand { margin-top: 62px; }
  .details {
    position: absolute;
    left: 0; right: 0;
    top: 178px;
    display: flex;
    justify-content: center;
    align-items: center;
    gap: 18px;
  }
  .person { text-align: right; }
  .person__name { color: var(--green); font-weight: 700; font-size: 22px; }
  .person__role, .person__company { color: var(--soft); font-size: 13px; margin-top: 3px; }
  .details__divider { width: 1px; height: 62px; background: var(--divider); }
  .contact { list-style: none; }
  .contact__item {
    display: flex; align-items: center; gap: 8px;
    color: var(--soft); font-size: 13px; line-height: 20px;
  }
  .contact__icon { width: 12px; height: 12px; flex: none; }
  .card__band {
    position: absolute; left: 0; right: 0; bottom: 0;
    height: 16px; background: var(--green);
  }
</style>
</head>
<body>
  <section class="card card--front" aria-label="Card front">
    <div class="brand">
      <span class="brand__dot"></span>
      <span class="brand__name">RIDGEVIEW RENEWAL</span>
    </div>
    <p class="tagline">YOUR <span class="tagline__accent">TAGLINE</span> HERE</p>
  </section>

  <section class="card card--back" aria-label="Card back">
    <div class="brand">
      <span class="brand__dot"></span>
      <span class="brand__name">RIDGEVIEW RENEWAL</span>
    </div>
    <div class="details">
      <div class="person">
        <p class="person__name">Daniel Harlow</p>
        <p class="person__role">Chief Operation Officer</p>
        <p class="person__company">Ridgeview Renewal LLC</p>
      </div>
      <span class="details__divider"></span>
      <ul class="contact">
        <li class="contact__item">
          <svg class="contact__icon" viewBox="0 0 12 12"><rect x="3" y="0.5" width="6" height="11" rx="1" fill="none" stroke="#12934a" stroke-width="1.2"/><circle cx="6" cy="9.6" r="0.7" fill="#12934a"/></svg>
          555.014.2200
        </li>
        <li class="contact__item">
          <svg class="contact__icon" viewBox="0 0 12 12"><rect x="0.5" y="2" width="11" height="8" fill="#12934a"/><path d="M0.5 2 6 6.5 11.5 2" fill="none" stroke="#2d2d2d" stroke-width="1"/></svg>
          dharlow@ridgeviewrenewal.com
        </li>
        <li class="contact__item">
          <svg class="contact__icon" viewBox="0 0 12 12"><circle cx="6" cy="6" r="5.5" fill="#12934a"/><path d="M0.5 6h11M6 0.5c-2.5 3-2.5 8 0 11M6 0.5c2.5 3 2.5 8 0 11" fill="none" stroke="#2d2d2d" stroke-width="0.8"/></svg>
          www.ridgeviewrenewal.com
        </li>
      </ul>
    </div>
    <div class="card__band"></div>
  </section>
</body>
</html>
```